Rig up a website for a Rigging Company

We already have a logo. Looking for a website design that works on plivano.com.
Our rigging company uses semi trucks, forklifts, and similar equipment to move large machines.
Our logo is white, black and red.

Target Market(s)

Medical Industry (moving medical equipment), Utility Industry (power equipment), Food Industry (moving bottling/packing equipment), US Government (large equipment)

Industry/Entity Type

It Company

Coding

Coded - Design and coding required

Number of Pages Required

5+ page

Font styles to use
Sans Serif

Colors
ec1f27
ffffff
0355a3

Requirements
Must have
• Home page, About page, Services Page, and Contact Information page
Nice to have
• Pictures of semi and forklifts and ability to insert our own pictures of our equipment

```html
<!DOCTYPE html>
<html lang="en">
<head>
<meta charset="utf-8">
<title>Harlow Rigging</title>
<link href="https://fonts.googleapis.com/css2?family=Roboto:ital,wght@0,300;0,400;0,500;0,700;1,300;1,400&display=swap" rel="stylesheet">
<style>
:root{
  --red:#e8393d;
  --red-light:#f27a7a;
  --grad:linear-gradient(100deg,#e8393d 0%,#f28080 100%);
  --white:#ffffff;
  --ink:#222222;
  --muted:#555555;
  --panel:#f0f0f0;
  --sky-top:#56606e;
  --sky-mid:#9aa3ad;
  --glow:#e6c9a4;
  --ground:#55575b;
}
*{box-sizing:border-box;margin:0;padding:0}
html,body{width:672px;height:1200px;overflow:hidden}
body{font-family:'Roboto',sans-serif;background:var(--white);color:var(--ink);position:relative}
.hero{position:absolute;left:0;top:0;width:672px;height:304px;
  background:
    radial-gradient(ellipse 150px 70px at 450px 220px,rgba(176,196,40,.55),rgba(176,196,40,0) 70%),
    radial-gradient(ellipse 200px 90px at 500px 150px,rgba(240,214,176,.75),rgba(240,214,176,0) 75%),
    linear-gradient(90deg,rgba(214,206,190,.85) 0%,rgba(190,170,130,.7) 30%,rgba(190,170,130,0) 42%),
    linear-gradient(180deg,var(--sky-top) 0%,var(--sky-mid) 30%,var(--glow) 58%,#8f8e8c 70%,var(--ground) 100%)}
.site-header{position:absolute;left:0;top:0;width:672px;height:38px;border-bottom:1px solid rgba(255,255,255,.3);display:flex;align-items:center;padding:0 29px}
.brand{font-weight:700;font-size:14px;color:var(--white);display:flex;align-items:center;gap:5px;width:203px}
.brand-dot{width:8px;height:8px;background:var(--red);border-radius:50%}
.nav{display:flex;gap:21px;font-size:9.5px;color:var(--white)}
.nav a{color:inherit;text-decoration:none}
.header-phone{margin-left:auto;font-size:8px;color:var(--white);font-weight:500}
.quote-btn{margin-left:11px;background:var(--white);color:var(--ink);font-size:7.5px;padding:5px 7px;border-radius:9px}
.welcome{position:absolute;left:0;top:304px;width:672px;height:62px;background:var(--grad);color:var(--white);text-align:center;padding:0 29px}
.welcome h1{font-size:13px;font-weight:500;margin-top:5px;padding-bottom:6px;border-bottom:1px dashed rgba(255,255,255,.8)}
.welcome p{font-size:6.6px;line-height:1.55;margin-top:10px}
.section{position:absolute;left:0;width:672px}
.section-title{position:absolute;left:29px;width:614px;text-align:center;font-size:12.5px;font-weight:500;padding-bottom:8px;border-bottom:1px dashed var(--red)}
.section-title span{color:var(--red)}
.services{top:366px;height:174px;background:var(--panel)}
.service{position:absolute;top:64px;width:142px;height:70px;border-radius:3px}
.service-icon{position:absolute;left:58px;top:-13px;width:26px;height:26px;border-radius:50%;background:var(--red);display:flex;align-items:center;justify-content:center}
.service-btn{position:absolute;left:6px;top:60px;width:130px;height:22px;background:var(--grad);color:var(--white);font-size:8.5px;display:flex;align-items:center;justify-content:center;border-radius:2px}
.gallery{top:540px;height:168px;background:var(--white)}
.gallery-strip{position:absolute;top:47px;left:0;display:flex;width:672px;height:105px}
.gallery-strip div{flex:1}
.testimonials{top:708px;height:238px;background:var(--panel)}
.quote{position:absolute;width:290px;display:flex;gap:16px;font-size:6.9px;line-height:1.6}
.quote p{font-style:italic;font-weight:300;color:var(--muted)}
.quote cite{display:block;font-style:normal;color:var(--ink);margin-top:4px;font-size:6.9px}
.quote .avatar{flex:none;width:43px;height:43px;border-radius:50%;background:linear-gradient(160deg,#d8d2cc,#8a7a70)}
.quote.left{text-align:right}
.divider-h{position:absolute;left:29px;top:118px;width:614px;border-top:1px dashed var(--red)}
.divider-v{position:absolute;left:336px;top:57px;height:118px;border-left:1px dashed var(--red)}
.skyline{position:absolute;left:0;top:206px;width:672px;height:32px;background:linear-gradient(0deg,rgba(232,57,61,.85),rgba(232,57,61,0) 100%)}
.site-footer{position:absolute;left:0;top:946px;width:672px;height:254px;background:var(--grad);color:var(--white)}
.fcol{position:absolute;top:31px;width:142px;font-size:7px;line-height:1.55}
.fcol h3{font-size:10px;font-weight:500;margin-bottom:10px}
.fcol p{margin-bottom:8px}
.social{display:flex;gap:8px;margin-top:10px}
.social span{width:6px;height:6px;border-radius:50%;background:var(--white)}
.field{background:var(--white);color:#999;font-size:6.5px;padding:0 7px;height:18px;display:flex;align-items:center;border-radius:2px;margin-bottom:11px}
.field-row{display:flex;gap:11px}.field-row .field{flex:1}
.field.area{height:36px;align-items:flex-start;padding-top:6px}
.send-btn{display:inline-block;background:var(--white);color:var(--ink);font-size:7px;padding:5px 10px;border-radius:2px}
.map{width:142px;height:126px;background:linear-gradient(135deg,#a9cbe8,#d9e4d0 55%,#b6d6a8)}
.footer-bar{position:absolute;left:29px;top:215px;width:614px;border-top:1px solid rgba(255,255,255,.7);display:flex;justify-content:space-between;align-items:center;padding-top:13px;font-size:6.8px;font-weight:500}
.footer-bar .brand{width:auto;font-size:13px;justify-content:center}
</style>
</head>
<body>
<div class="hero" role="img" aria-label="Forklift carrying a wooden crate in front of a warehouse at a port at dusk"></div>
<header class="site-header">
  <div class="brand"><span class="brand-dot"></span>Harlow Rigging</div>
  <nav class="nav"><a>HOME</a><a>ABOUT US</a><a>SERVICES</a><a>CONTACT</a></nav>
  <div class="header-phone">+1 800 555 02 17</div>
  <div class="quote-btn">Request a Quote</div>
</header>

<section class="welcome">
  <h1>Welcome to Harlow Rigging</h1>
  <p>Sed ut perspiciatis unde omnis iste natus error sit voluptatem accusantium doloremque laudantium, totam rem aperiam, eaque ipsa quae ab illo inventore veritatis et quasi architecto beatae vitae dicta sunt explicabo.</p>
</section>

<section class="section services">
  <h2 class="section-title" style="top:8px">Our <span>Services</span></h2>
  <div class="service" style="left:29px;background:linear-gradient(120deg,#e0b060,#3a5fa0)" role="img" aria-label="Semi truck on a highway">
    <div class="service-icon"><svg width="12" height="9" viewBox="0 0 12 9"><rect x="0" y="1" width="7" height="5" fill="#fff"/><rect x="7" y="3" width="4" height="3" fill="#fff"/><circle cx="3" cy="7.5" r="1.2" fill="#fff"/><circle cx="9" cy="7.5" r="1.2" fill="#fff"/></svg></div>
    <div class="service-btn">Ground Shipping</div>
  </div>
  <div class="service" style="left:186px;background:linear-gradient(120deg,#3a3230,#8a6a48)" role="img" aria-label="Forklift moving boxes in a warehouse">
    <div class="service-icon"><svg width="12" height="11" viewBox="0 0 12 11"><rect x="1" y="4" width="10" height="6" fill="#fff"/><path d="M3 4 L6 1 L9 4" stroke="#fff" fill="none"/></svg></div>
    <div class="service-btn">Forwarding Services</div>
  </div>
  <div class="service" style="left:344px;background:linear-gradient(120deg,#5a4a40,#c09070)" role="img" aria-label="Warehouse aisle with stocked shelves">
    <div class="service-icon"><svg width="12" height="10" viewBox="0 0 12 10"><rect x="1" y="1" width="10" height="8" rx="1" fill="#fff"/><rect x="5" y="3" width="2" height="3" fill="#e8393d"/></svg></div>
    <div class="service-btn">Packaged Goods</div>
  </div>
  <div class="service" style="left:501px;background:linear-gradient(120deg,#6a5e56,#d0b090)" role="img" aria-label="Warehouse shelving with a worker">
    <div class="service-icon"><svg width="11" height="12" viewBox="0 0 11 12"><rect x="1" y="1" width="9" height="10" fill="#fff"/><path d="M3 4H8M3 6H8M3 8H8" stroke="#e8393d"/></svg></div>
    <div class="service-btn">Warehousing</div>
  </div>
</section>

<section class="section gallery">
  <h2 class="section-title" style="top:10px">Our <span>Gallery</span></h2>
  <div class="gallery-strip">
    <div style="background:linear-gradient(135deg,#9aa6b0,#dfe3e6)" role="img" aria-label="Large warehouse interior"></div>
    <div style="background:linear-gradient(135deg,#3d78b8,#7a6a40)" role="img" aria-label="Truck on a coastal road"></div>
    <div style="background:linear-gradient(135deg,#a8c4dc,#d07040)" role="img" aria-label="Shipping containers being lifted"></div>
    <div style="background:linear-gradient(135deg,#d08a40,#3a3030)" role="img" aria-label="Cargo ship at a port at sunset"></div>
    <div style="background:linear-gradient(135deg,#b0b8c4,#a04848)" role="img" aria-label="Loading docks with trucks"></div>
  </div>
</section>

<section class="section testimonials">
  <h2 class="section-title" style="top:10px">What <span>People Say</span></h2>
  <div class="divider-v"></div>
  <div class="divider-h"></div>
  <div class="quote left" style="left:29px;top:56px"><div><p>Duis aute irure dolor in reprehenderit in voluptate velit esse cillum dolore eu fugiat nulla pariatur. Excepteur sint occaecat cupidatat non proident, sunt in culpa qui officia deserunt mollit.</p><cite>Dan Corwin, Operations Manager</cite></div><div class="avatar" role="img" aria-label="Portrait of Dan Corwin"></div></div>
  <div class="quote" style="left:355px;top:56px"><div class="avatar" role="img" aria-label="Portrait of Lena Graves"></div><div><p>Provident, similique sunt in culpa qui officia deserunt mollitia animi, id est laborum et dolorum fuga. Et harum quidem rerum facilis est et expedita distinctio. Nam libero tempore, cum soluta nobis.</p><cite>Lena Graves, Creative Designer</cite></div></div>
  <div class="quote left" style="left:29px;top:134px"><div><p>Luis aute irure dolor in reprehenderit in piluptate velit esse cillum dolore eu fugiat nulla pariatur. Excepteur sint occaecat cupidatat non proident, sunt in culpa qui officia deserunt mollit.</p><cite>Marta Lind, Manager</cite></div><div class="avatar" role="img" aria-label="Portrait of Marta Lind"></div></div>
  <div class="quote" style="left:355px;top:134px"><div class="avatar" role="img" aria-label="Portrait of Tim Larkin"></div><div><p>At vero eos et accusamus et iusto odio dignissimos ducimus qui blanditiis praesentium voluptatum deleniti atque corrupti quos dolores et quas molestias excepturi sint occaecati asperiores.</p><cite>Tim Larkin, Developer</cite></div></div>
  <div class="skyline" role="img" aria-label="City skyline and airport silhouette"></div>
</section>

<footer class="site-footer">
  <div class="fcol" style="left:29px">
    <h3>Contact Us</h3>
    <p>Please feel free to contact us for any issue. Our staff is available to you from 9AM until 5PM on weekdays.</p>
    <p><b style="font-weight:500">Phone:</b> +1 800-555-0163</p>
    <p><b style="font-weight:500">Office:</b> Pier 9 Freight Yard</p>
    <p><b style="font-weight:500">Email:</b> info@plivano.com</p>
    <div class="social"><span></span><span></span><span></span><span></span><span></span></div>
  </div>
  <div class="fcol" style="left:186px">
    <h3>Feel Free to Mail</h3>
    <div class="field-row"><div class="field">Name *</div><div class="field">Email *</div></div>
    <div class="field">Subject</div>
    <div class="field area">Write Your Message Here...</div>
    <div class="send-btn">SEND MESSAGE</div>
  </div>
  <div class="fcol" style="left:344px">
    <h3>Headquarters</h3>
    <div class="map" role="img" aria-label="Map showing the headquarters location"></div>
  </div>
  <div class="fcol" style="left:502px">
    <h3>About Team</h3>
    <p>Enim congue blandit. Lorem ipsum dolor sit amet, consectetur adipiscing elit. Quisque consectetur interdum finibus. Vestibulum ante ipsum primis in faucibus orci. luctus et ultrices posuere.</p>
    <p>Cubilia cras blandit finibus ipsum, id porttitor arcu volutpat a. Integer iaculis erat nec justo malesuada faucibus vel tempus sapien. Vivamus aliquam euismod tristique.</p>
  </div>
  <div class="footer-bar">
    <span>Copyright © 2017 Harlow Rigging</span>
    <span class="brand">Harlow Rigging</span>
    <span>All rights reserved</span>
  </div>
</footer>
</body>
</html>
```